Powerpoint Presentation Template

Kindly design a business class Powepoint Presentation template for our business use. Please stick to our company colours or even pictures as shown on our website and Logo

```html
<!DOCTYPE html>
<html lang="en">
<head>
<meta charset="utf-8">
<title>Stonecrest Properties – Presentation Template</title>
<link href="https://fonts.googleapis.com/css2?family=Open+Sans:wght@300;400;600;700&display=swap" rel="stylesheet">
<style>
:root{
  --red:#8c2b1f;
  --red-soft:rgba(140,43,31,.88);
  --dark:#2e3033;
  --dark2:#3b3d40;
  --grey:#6b6d70;
  --light:#f4f4f4;
  --line:#dcdcdc;
  --text:#555;
}
*{box-sizing:border-box;margin:0;padding:0}
html,body{width:797px;height:1200px;overflow:hidden;background:#e9e9e9;font-family:"Open Sans",Arial,sans-serif;color:var(--text)}
.deck{display:grid;grid-template-columns:repeat(3,260px);grid-auto-rows:146px;gap:4px 5px;padding:2px 3px}
.slide{position:relative;background:#fff;overflow:hidden}
.slide.num::after{content:"";position:absolute;top:0;right:0;border-style:solid;border-width:0 16px 16px 0;border-color:transparent var(--red) transparent transparent}
.foot{position:absolute;left:8px;right:8px;bottom:3px;display:flex;justify-content:space-between;align-items:center;font-size:3px;color:#999}
.foot .brand{font-size:4px;font-weight:700;color:var(--red);letter-spacing:.2px}
.foot .mark{width:14px;height:3px;background:#ccc}
.title{position:absolute;top:10px;left:12px;font-size:8.5px;font-weight:400;color:var(--red);text-transform:uppercase;letter-spacing:.2px}
.ph{background:linear-gradient(160deg,#b8b3ad,#7d746c 60%,#5a524c)}
.ph.warm{background:linear-gradient(160deg,#c89b7b,#8b4a35 55%,#4d3a33)}
.ph.grey{background:linear-gradient(180deg,#dcdcdc,#9a9a9a 60%,#5e5e5e)}
.ph.sky{background:linear-gradient(180deg,#c9d2d8,#a5a39c 55%,#6e6257)}
.tiny{font-size:3.2px;line-height:1.45;color:#777}
.tiny.w{color:#f1e6e4}
.abs{position:absolute}
.ico{display:inline-block;border-radius:50%;background:var(--red)}

/* slide 1 */
.cols{display:grid;grid-template-columns:repeat(5,1fr);height:100%}
.cols div{padding:34px 4px 0;color:#fff;text-align:center}
.cols div:nth-child(1){background:#1f2022}.cols div:nth-child(2){background:#2a2b2d}
.cols div:nth-child(3){background:#36383a}.cols div:nth-child(4){background:#434547}
.cols div:nth-child(5){background:var(--red)}
.cols svg{width:18px;height:18px;margin-bottom:20px}
.cols h4{font-size:6px;font-weight:400;margin-bottom:3px}
.cols p{font-size:3px;line-height:1.45;color:#ddd;text-align:left}

/* mock up points */
.point{position:absolute;left:140px;width:110px}
.point b{display:block;font-size:4.5px;font-weight:400;color:#fff;padding:1px 3px;background:var(--red)}
.point b.dk{background:var(--dark)}

/* right picture */
.ring{position:absolute;left:35px;top:18px;width:62px;height:62px;border:2px solid #fff;border-radius:50%;display:flex;align-items:center;justify-content:center;text-align:center;color:#fff;font-size:7px;line-height:1.2}
.heading-box{position:absolute;display:flex;flex-direction:column;align-items:center;justify-content:center;color:#fff;text-align:center;padding:4px}
.heading-box h5{font-size:6px;font-weight:400;margin-bottom:2px}
.overlay-title{font-size:11px;font-weight:400;color:#fff;line-height:1.2}
.sub{font-size:3.5px;color:#f0d9d5;margin-top:2px}
.stat{font-size:13px;color:var(--dark);font-weight:300}
.pill{display:inline-flex;align-items:center;gap:4px;background:var(--red);color:#fff;font-size:6px;padding:3px 6px;border-radius:2px}
.pill.dk{background:var(--dark)}
.price{position:absolute;top:34px;width:52px;height:92px;background:#fff;box-shadow:0 1px 3px rgba(0,0,0,.25);text-align:center}
.price .hd{background:var(--dark2);color:#fff;font-size:9px;padding:4px 0 3px}
.price .hd small{display:block;font-size:2.6px}
.price .row{font-size:2.8px;color:#888;border-bottom:1px solid #eee;padding:2.5px 0}
table{border-collapse:collapse;width:236px}
td,th{font-size:3px;text-align:center;padding:1.6px 0;border-bottom:1px solid #eee;color:#777}
th{background:var(--red);color:#fff;font-weight:400}
td:first-child{color:var(--red);text-align:left;padding-left:4px}
.face{border-radius:50%;background:linear-gradient(160deg,#d6d3cf,#8f8a85)}
.person{position:absolute;display:flex;gap:5px;width:110px}
.person h6{font-size:5px;font-weight:400;color:var(--dark)}
.person .role{font-size:3px;color:var(--red)}
</style>
</head>
<body>
<main class="deck">

<!-- 1 Five headings -->
<section class="slide">
  <div class="cols">
    <div><svg viewBox="0 0 20 20" fill="none" stroke="#fff" stroke-width="1"><circle cx="10" cy="10" r="5"/><circle cx="10" cy="10" r="2"/></svg><h4>Heading Here</h4><p>Lorem ipsum dolor sit amet, consectetur adipiscing elit, sed do eiusmod tempor incididunt ut labore et dolore magna aliqua.</p></div>
    <div><svg viewBox="0 0 20 20" fill="none" stroke="#fff" stroke-width="1"><rect x="4" y="5" width="12" height="8"/><path d="M7 16h6M10 13v3"/></svg><h4>Heading Here</h4><p>Lorem ipsum dolor sit amet, consectetur adipiscing elit, sed do eiusmod tempor incididunt ut labore et dolore magna aliqua.</p></div>
    <div><svg viewBox="0 0 20 20" fill="none" stroke="#fff" stroke-width="1"><circle cx="9" cy="9" r="4"/><path d="M12 12l4 4"/></svg><h4>Heading Here</h4><p>Lorem ipsum dolor sit amet, consectetur adipiscing elit, sed do eiusmod tempor incididunt ut labore et dolore magna aliqua.</p></div>
    <div><svg viewBox="0 0 20 20" fill="none" stroke="#fff" stroke-width="1"><rect x="5" y="5" width="10" height="10"/><circle cx="10" cy="10" r="2"/></svg><h4>Heading Here</h4><p>Lorem ipsum dolor sit amet, consectetur adipiscing elit, sed do eiusmod tempor incididunt ut labore et dolore magna aliqua.</p></div>
    <div><svg viewBox="0 0 20 20" fill="none" stroke="#fff" stroke-width="1"><circle cx="10" cy="10" r="7"/><circle cx="10" cy="10" r="3"/></svg><h4>Heading Here</h4><p>Lorem ipsum dolor sit amet, consectetur adipiscing elit, sed do eiusmod tempor incididunt ut labore et dolore magna aliqua.</p></div>
  </div>
</section>

<!-- 2 Mock up -->
<section class="slide num">
  <h2 class="title">Mock Up</h2>
  <div class="abs ph warm" style="left:12px;top:26px;width:120px;height:86px" role="img" aria-label="Laptop and desktop screens showing a modern property photo"></div>
  <div class="point" style="top:32px"><b>1 POINT</b><p class="tiny">This is a sample text. Add your own text and description here.</p></div>
  <div class="point" style="top:56px"><b class="dk">2 POINT</b><p class="tiny">This is a sample text. Add your own text and description here.</p></div>
  <div class="point" style="top:80px"><b>3 POINT</b><p class="tiny">This is a sample text. Add your own text and description here.</p></div>
  <footer class="foot"><span class="brand">STONECREST</span><span>© Copyright Stonecrest Properties</span><span class="mark"></span></footer>
</section>

<!-- 3 Right picture slide -->
<section class="slide num">
  <div class="abs" style="left:0;top:0;width:130px;height:146px;background:var(--red)"></div>
  <div class="ring">RIGHT<br>PICTURE<br>SLIDE</div>
  <p class="tiny w abs" style="left:22px;top:96px;width:90px;text-align:center">Mauris quam dolor, cursus at porta et, luctus eget purus. Nunc tempor luctus interdum. Duis libero dignissim.</p>
  <svg class="abs" style="left:150px;top:22px" width="100" height="55" viewBox="0 0 100 55">
    <g fill="var(--red)"><rect x="2" y="25" width="4" height="28"/><rect x="24" y="15" width="4" height="38"/><rect x="46" y="30" width="4" height="23"/><rect x="68" y="10" width="4" height="43"/></g>
    <g fill="var(--dark)"><rect x="8" y="32" width="4" height="21"/><rect x="30" y="5" width="4" height="48"/><rect x="52" y="18" width="4" height="35"/><rect x="74" y="24" width="4" height="29"/></g>
    <g fill="#aaa"><rect x="14" y="40" width="4" height="13"/><rect x="36" y="36" width="4" height="17"/><rect x="58" y="42" width="4" height="11"/><rect x="80" y="2" width="4" height="51"/></g>
  </svg>
  <div class="abs stat" style="left:150px;top:84px"><span style="color:var(--red);font-size:8px">▲</span> 85%</div>
  <div class="abs" style="left:158px;top:104px;font-size:4px;color:var(--dark);font-weight:600">Profit</div>
  <p class="tiny abs" style="left:158px;top:110px;width:60px">Mauris quam dolor, cursus at porta et, luctus eget purus.</p>
  <footer class="foot" style="left:140px"><span></span><span class="mark"></span></footer>
</section>

<!-- 4 Our mockup area -->
<section class="slide">
  <div class="abs" style="left:0;top:0;width:260px;height:62px;background:var(--red)"></div>
  <h2 class="title" style="color:#fff">Our Mockup Area</h2>
  <div class="abs" style="left:12px;top:32px;font-size:4.5px;color:#fff">Heading Here</div>
  <p class="tiny w abs" style="left:12px;top:40px;width:105px">Lorem ipsum dolor sit amet, consectetur adipiscing elit, sed do eiusmod tempor incididunt ut labore.</p>
  <div class="abs" style="left:112px;top:12px;width:140px;height:100px;background:#222;border-radius:3px;padding:5px">
    <div class="ph sky" style="width:100%;height:100%" role="img" aria-label="Monitor screen showing a modern office building with umbrellas"></div>
  </div>
  <div class="abs" style="left:170px;top:112px;width:24px;height:14px;background:#ccc"></div>
  <span class="ico abs" style="left:12px;top:74px;width:7px;height:7px"></span>
  <p class="tiny abs" style="left:22px;top:73px;width:85px">Lorem ipsum dolor sit amet, consectetur adipiscing elit, sed do eiusmod tempor.</p>
  <span class="ico abs" style="left:12px;top:94px;width:7px;height:7px;background:var(--dark)"></span>
  <p class="tiny abs" style="left:22px;top:93px;width:85px">Lorem ipsum dolor sit amet, consectetur adipiscing elit, sed do eiusmod tempor.</p>
  <footer class="foot"><span class="brand">STONECREST</span><span>© Copyright Stonecrest Properties</span><span class="mark"></span></footer>
</section>

<!-- 5 Title grid -->
<section class="slide num">
  <h2 class="title">Your Title Goes Here</h2>
  <div class="abs ph" style="left:18px;top:34px;width:71px;height:42px" role="img" aria-label="Apartment block exterior"></div>
  <div class="heading-box" style="left:93px;top:34px;width:71px;height:42px;background:var(--dark)"><h5>Heading Goes Here</h5><p class="tiny w">Lorem ipsum dolor sit amet, consectetur adipiscing elit.</p></div>
  <div class="abs ph warm" style="left:168px;top:34px;width:71px;height:42px" role="img" aria-label="Row of townhouses"></div>
  <div class="heading-box" style="left:18px;top:80px;width:71px;height:42px;background:var(--red)"><h5>Heading Goes Here</h5><p class="tiny w">Lorem ipsum dolor sit amet, consectetur adipiscing elit.</p></div>
  <div class="abs ph sky" style="left:93px;top:80px;width:71px;height:42px" role="img" aria-label="Construction site with workers"></div>
  <div class="heading-box" style="left:168px;top:80px;width:71px;height:42px;background:var(--dark)"><h5>Heading Goes Here</h5><p class="tiny w">Lorem ipsum dolor sit amet, consectetur adipiscing elit.</p></div>
  <footer class="foot"><span class="brand">STONECREST</span><span>© Copyright Stonecrest Properties</span><span class="mark"></span></footer>
</section>

<!-- 6 About us -->
<section class="slide">
  <div class="abs ph grey" style="inset:0" role="img" aria-label="Industrial warehouse exterior"></div>
  <div class="abs" style="right:0;top:34px;width:130px;height:92px;background:var(--red-soft);padding:18px 12px">
    <div style="font-size:8px;color:#fff;margin-bottom:6px">ABOUT US</div>
    <p class="tiny w">Lorem ipsum dolor sit amet, consectetur adipiscing elit, sed do eiusmod tempor incididunt ut labore et dolore magna aliqua. Ut enim ad minim veniam, quis nostrud exercitation ullamco laboris nisi ut aliquip ex ea commodo consequat.</p>
  </div>
</section>

<!-- 7 Divider -->
<section class="slide">
  <div class="abs ph grey" style="inset:0;background:linear-gradient(150deg,#6a6a6a,#2e2e2e 70%,#555)" role="img" aria-label="Heavy truck at a construction site"></div>
  <div class="abs" style="left:125px;top:0;width:110px;height:120px;background:var(--red-soft);padding:44px 12px 0">
    <div class="overlay-title">THIS IS YOUR<br>DIVIDER PAGE</div>
    <div class="sub">YOUR SUBTITLE GOES HERE</div>
  </div>
</section>

<!-- 8 Divider 2 -->
<section class="slide">
  <div class="abs ph grey" style="inset:0" role="img" aria-label="Modern curved office building"></div>
  <div class="abs" style="left:14px;top:0;width:58px;height:146px;background:var(--red)"></div>
  <div class="abs" style="left:90px;top:76px;text-align:right;width:158px">
    <div class="overlay-title">THIS IS YOUR DIVIDER PAGE</div>
    <div class="sub" style="color:var(--red)">YOUR SUBTITLE GOES HERE</div>
  </div>
</section>

<!-- 9 Quote -->
<section class="slide num">
  <h2 class="title">Quote Area</h2>
  <div class="abs ph sky" style="left:120px;top:36px;width:140px;height:90px" role="img" aria-label="Aerial view of a housing estate"></div>
  <div class="abs" style="left:0;top:36px;width:130px;height:90px;background:var(--red);padding:22px 10px;color:#fff;font-size:5.3px;line-height:1.35">“ Coming together is a beginning. Keeping together is progress. Working together is success. ”<br><br>– Walter Brandt</div>
  <footer class="foot"><span class="brand">STONECREST</span><span>© Copyright Stonecrest Properties</span><span class="mark"></span></footer>
</section>

<!-- 10 Brand detailed -->
<section class="slide num">
  <h2 class="title">Brand Detailed</h2>
  <div class="abs ph warm" style="left:16px;top:30px;width:124px;height:94px" role="img" aria-label="Red and grey multi-storey building"></div>
  <div class="heading-box" style="left:144px;top:30px;width:52px;height:45px;background:var(--red)"><h5 style="font-size:4.5px">System</h5><p class="tiny w">Mauris quam dolor, cursus at porta et, luctus eget purus.</p></div>
  <div class="heading-box" style="left:199px;top:30px;width:52px;height:45px;background:var(--dark)"><h5 style="font-size:4.5px">Technology</h5><p class="tiny w">Mauris quam dolor, cursus at porta et, luctus eget purus.</p></div>
  <div class="heading-box" style="left:144px;top:79px;width:52px;height:45px;background:var(--dark)"><h5 style="font-size:4.5px">Leisure</h5><p class="tiny w">Mauris quam dolor, cursus at porta et, luctus eget purus.</p></div>
  <div class="heading-box" style="left:199px;top:79px;width:52px;height:45px;background:var(--red)"><h5 style="font-size:4.5px">Digital</h5><p class="tiny w">Mauris quam dolor, cursus at porta et, luctus eget purus.</p></div>
  <footer class="foot"><span class="brand">STONECREST</span><span>© Copyright Stonecrest Properties</span><span class="mark"></span></footer>
</section>

<!-- 11 Product philosophy -->
<section class="slide num">
  <h2 class="title">Product Philosophy</h2>
  <svg class="abs" style="left:95px;top:42px" width="70" height="70" viewBox="0 0 70 70">
    <circle cx="35" cy="35" r="27" fill="none" stroke="var(--red)" stroke-width="14" stroke-dasharray="169.6" transform="rotate(-90 35 35)"/>
    <circle cx="35" cy="35" r="27" fill="none" stroke="var(--dark)" stroke-width="14" stroke-dasharray="25.4 144.2" transform="rotate(-90 35 35)"/>
    <circle cx="35" cy="35" r="27" fill="none" stroke="var(--dark2)" stroke-width="14" stroke-dasharray="42.4 127.2" stroke-dashoffset="-25.4" transform="rotate(-90 35 35)"/>
    <circle cx="35" cy="35" r="13" fill="var(--red)"/>
    <g font-size="4.5" fill="#fff" text-anchor="middle"><text x="49" y="16">15%</text><text x="60" y="40">25%</text><text x="35" y="64">20%</text><text x="10" y="34">40%</text></g>
  </svg>
  <div class="abs" style="left:20px;top:44px;width:60px;text-align:right"><div style="font-size:3.6px;color:var(--red)">Secure</div><p class="tiny">Nullam eu tempor purus. Nunc a leo magna.</p></div>
  <span class="ico abs" style="left:84px;top:46px;width:14px;height:14px"></span>
  <div class="abs" style="left:20px;top:92px;width:60px;text-align:right"><div style="font-size:3.6px;color:var(--red)">Good Package</div><p class="tiny">Nullam eu tempor purus. Nunc a leo magna.</p></div>
  <span class="ico abs" style="left:84px;top:92px;width:14px;height:14px"></span>
  <span class="ico abs" style="left:178px;top:46px;width:14px;height:14px;background:var(--dark)"></span>
  <div class="abs" style="left:196px;top:44px;width:56px"><div style="font-size:3.6px;color:var(--dark)">Well Organized</div><p class="tiny">Nullam eu tempor purus. Nunc a leo magna.</p></div>
  <span class="ico abs" style="left:178px;top:92px;width:14px;height:14px;background:var(--dark)"></span>
  <div class="abs" style="left:196px;top:90px;width:56px"><div style="font-size:3.6px;color:var(--dark)">Publication</div><p class="tiny">Nullam eu tempor purus. Nunc a leo magna.</p></div>
  <footer class="foot"><span class="brand">STONECREST</span><span>© Copyright Stonecrest Properties</span><span class="mark"></span></footer>
</section>

<!-- 12 Regional chart -->
<section class="slide">
  <div class="abs" style="left:0;top:0;width:260px;height:100px;background:linear-gradient(180deg,#fdfdfd,#d7d7d7)" role="img" aria-label="Faded city skyline backdrop"></div>
  <svg class="abs" style="left:0;top:18px" width="260" height="82" viewBox="0 0 260 82">
    <g fill="var(--red)"><rect x="30" y="42" width="10" height="40"/><rect x="104" y="22" width="10" height="60"/><rect x="154" y="53" width="10" height="29"/><rect x="198" y="62" width="10" height="20"/></g>
    <g fill="var(--dark)"><rect x="52" y="32" width="10" height="50"/><rect x="82" y="52" width="10" height="30"/><rect x="176" y="62" width="10" height="20"/><rect x="220" y="72" width="10" height="10"/></g>
    <g font-size="4" fill="#333" text-anchor="middle"><text x="35" y="40">400</text><text x="57" y="30">500</text><text x="87" y="50">300</text><text x="109" y="20">600</text><text x="159" y="51">290</text><text x="181" y="60">200</text><text x="203" y="60">200</text><text x="225" y="70">100</text></g>
  </svg>
  <div class="abs" style="left:0;top:100px;width:260px;height:30px;background:#1f2022;display:grid;grid-template-columns:repeat(5,1fr);padding:3px 6px;text-align:center;color:#fff">
    <div><div style="font-size:4px">Asia</div><p class="tiny w">Duis quis purus adipiscing nisl.</p></div>
    <div><div style="font-size:4px">Africa</div><p class="tiny w">Duis quis purus adipiscing nisl.</p></div>
    <div><div style="font-size:4px">America</div><p class="tiny w">Duis quis purus adipiscing nisl.</p></div>
    <div><div style="font-size:4px">Asia</div><p class="tiny w">Duis quis purus adipiscing nisl.</p></div>
    <div><div style="font-size:4px">Euro</div><p class="tiny w">Duis quis purus adipiscing nisl.</p></div>
  </div>
  <footer class="foot"><span class="brand">STONECREST</span><span>© Copyright Stonecrest Properties</span><span class="mark"></span></footer>
</section>

<!-- 13 Trending -->
<section class="slide num">
  <h2 class="title">Trending in the World</h2>
  <div class="abs" style="left:12px;top:34px;width:160px;height:88px;background:radial-gradient(ellipse at center,#cfcfcf,#e9e9e9 70%,#fff)" role="img" aria-label="World map in grey"></div>
  <div class="abs" style="left:24px;top:72px;width:18px;height:18px;border-radius:50%;background:var(--red);color:#fff;font-size:5px;display:flex;align-items:center;justify-content:center">25%</div>
  <div class="abs" style="left:70px;top:54px;width:24px;height:24px;border-radius:50%;background:var(--dark);color:#fff;font-size:8px;display:flex;align-items:center;justify-content:center">80%</div>
  <div class="abs" style="left:140px;top:54px;width:26px;height:26px;border-radius:50%;background:var(--red);color:#fff;font-size:8px;display:flex;align-items:center;justify-content:center">75%</div>
  <div class="abs" style="left:120px;top:82px;width:14px;height:14px;border-radius:50%;background:var(--dark2);color:#fff;font-size:4px;display:flex;align-items:center;justify-content:center">15%</div>
  <span class="ico abs" style="left:184px;top:44px;width:11px;height:11px;background:#fff;border:1px solid var(--red)"></span>
  <div class="abs" style="left:200px;top:40px;width:52px"><div style="font-size:3.6px;color:var(--red)">Confusion</div><p class="tiny">Nullam eu tempor purus.</p></div>
  <span class="ico abs" style="left:184px;top:70px;width:11px;height:11px;background:#fff;border:1px solid var(--dark)"></span>
  <div class="abs" style="left:200px;top:66px;width:52px"><div style="font-size:3.6px;color:var(--dark)">Intangible</div><p class="tiny">Nullam eu tempor purus.</p></div>
  <span class="ico abs" style="left:184px;top:96px;width:11px;height:11px;background:#fff;border:1px solid var(--dark)"></span>
  <div class="abs" style="left:200px;top:92px;width:52px"><div style="font-size:3.6px;color:var(--dark)">Performance</div><p class="tiny">Nullam eu tempor purus.</p></div>
  <footer class="foot"><span class="brand">STONECREST</span><span>© Copyright Stonecrest Properties</span><span class="mark"></span></footer>
</section>

<!-- 14 Africa map -->
<section class="slide num">
  <h2 class="title">Africa Map</h2>
  <div class="abs" style="left:8px;top:24px;width:110px;height:110px;background:radial-gradient(ellipse at 45% 45%,#8c2b1f 0 18%,#d8d8d8 19% 55%,#fff 70%)" role="img" aria-label="Map of Africa with highlighted countries"></div>
  <div class="abs" style="left:126px;top:30px;font-size:3.5px;color:#888">ELEMENT TITLE HERE</div>
  <p class="tiny abs" style="left:126px;top:38px;width:120px">Lorem ipsum is simply dummy text of the printing and typesetting industry, standard since the sixteenth century.</p>
  <span class="pill dk abs" style="left:126px;top:64px">▮ 50%</span>
  <span class="pill abs" style="left:168px;top:64px">▮ 50%</span>
  <p class="tiny abs" style="left:126px;top:90px;width:110px">Lorem ipsum is simply dummy text of the printing and typesetting industry.</p>
  <footer class="foot"><span class="brand">STONECREST</span><span>© Copyright Stonecrest Properties</span><span class="mark"></span></footer>
</section>

<!-- 15 South Africa map -->
<section class="slide num">
  <h2 class="title">South Africa Map</h2>
  <div class="abs" style="left:12px;top:30px;font-size:3.5px;color:#888">ELEMENT TITLE HERE</div>
  <p class="tiny abs" style="left:12px;top:38px;width:110px">Lorem ipsum is simply dummy text of the printing and typesetting industry, standard since the sixteenth century.</p>
  <span class="pill dk abs" style="left:12px;top:68px">▮ 50%</span>
  <span class="pill abs" style="left:56px;top:68px">▮ 50%</span>
  <p class="tiny abs" style="left:12px;top:94px;width:110px">Lorem ipsum is simply dummy text of the printing and typesetting industry.</p>
  <div class="abs" style="left:130px;top:28px;width:125px;height:95px;background:radial-gradient(ellipse at 50% 55%,#1a1a1a 0 22%,#dcdcdc 23% 48%,#8c2b1f 49% 55%,#fff 68%)" role="img" aria-label="Map of South Africa with highlighted provinces"></div>
  <footer class="foot"><span class="brand">STONECREST</span><span>© Copyright Stonecrest Properties</span><span class="mark"></span></footer>
</section>

<!-- 16 Three column description -->
<section class="slide num">
  <h2 class="title">Three Column Description</h2>
  <p class="abs" style="left:12px;top:26px;width:230px;font-size:5px;color:var(--red);line-height:1.3">This is place for your header text. Insert your text here, just replace this text with your own text</p>
  <div class="abs" style="left:12px;top:50px;width:236px;display:grid;grid-template-columns:repeat(3,1fr);gap:10px">
    <p class="tiny">Lorem ipsum dolor sit amet, consectetur adipiscing elit, sed do eiusmod tempor incididunt ut labore et dolore magna aliqua. Ut enim ad minim veniam, quis nostrud exercitation ullamco laboris.<br><br>Duis aute irure dolor in reprehenderit in voluptate velit esse cillum dolore.</p>
    <p class="tiny">Lorem ipsum dolor sit amet, consectetur adipiscing elit, sed do eiusmod tempor incididunt ut labore et dolore magna aliqua. Ut enim ad minim veniam, quis nostrud exercitation ullamco laboris.<br><br>Duis aute irure dolor in reprehenderit in voluptate velit esse cillum dolore.</p>
    <p class="tiny">Lorem ipsum dolor sit amet, consectetur adipiscing elit, sed do eiusmod tempor incididunt ut labore et dolore magna aliqua. Ut enim ad minim veniam, quis nostrud exercitation ullamco laboris.<br><br>Duis aute irure dolor in reprehenderit in voluptate velit esse cillum dolore.</p>
  </div>
  <footer class="foot"><span class="brand">STONECREST</span><span>© Copyright Stonecrest Properties</span><span class="mark"></span></footer>
</section>

<!-- 17 Our team single -->
<section class="slide num">
  <h2 class="title">Our Team</h2>
  <div class="abs face" style="left:98px;top:24px;width:62px;height:62px" role="img" aria-label="Portrait photo of team member"></div>
  <div class="abs" style="left:60px;top:92px;width:140px;text-align:center">
    <div style="font-size:3.6px;color:var(--dark)">Mr. John Smith</div>
    <div style="font-size:3px;color:var(--red)">CEO</div>
    <p class="tiny">Lorem ipsum dolor sit amet, consectetur adipiscing elit, sed do eiusmod tempor incididunt ut labore.</p>
    <div style="display:flex;gap:2px;justify-content:center;margin-top:2px"><span class="ico" style="width:4px;height:4px"></span><span class="ico" style="width:4px;height:4px"></span><span class="ico" style="width:4px;height:4px"></span><span class="ico" style="width:4px;height:4px"></span></div>
  </div>
  <footer class="foot"><span class="brand">STONECREST</span><span>© Copyright Stonecrest Properties</span><span class="mark"></span></footer>
</section>

<!-- 18 Monthly subscription -->
<section class="slide num">
  <h2 class="title">Monthly Subscription</h2>
  <div class="abs" style="left:0;top:50px;width:260px;height:90px;background:var(--red)"></div>
  <div class="price" style="left:40px"><div class="hd">$300<small>per month</small></div><div class="row">Unique Edition</div><div class="row">High Cloud Service</div><div class="row">3 User</div><div class="row">Free Update</div></div>
  <div class="price" style="left:96px;top:28px;height:100px"><div class="hd" style="background:#111">$900<small>per month</small></div><div class="row">Business Edition</div><div class="row">High Cloud Service</div><div class="row">6 User</div><div class="row">Free Update</div></div>
  <div class="price" style="left:152px"><div class="hd">$400<small>per month</small></div><div class="row">Unique Edition</div><div class="row">High Cloud Service</div><div class="row">3 User</div><div class="row">Free Update</div></div>
</section>

<!-- 19 Table -->
<section class="slide num">
  <h2 class="title">Your Title Goes Here</h2>
  <p class="tiny abs" style="left:12px;top:24px;width:150px">Description: There are many variations of passages available, most have been altered.</p>
  <table class="abs" style="left:12px;top:38px">
    <tr><th>Lorem ipsum</th><th>Value</th><th>Value</th><th>Value</th><th>Value</th></tr>
    <tr><td>Lorem ipsum</td><td>10</td><td>15</td><td>16</td><td>18</td></tr>
    <tr><td>Lorem ipsum</td><td>12</td><td>11</td><td>15</td><td>15</td></tr>
    <tr><td>Lorem ipsum</td><td>20</td><td>22</td><td>23</td><td>21</td></tr>
    <tr><td>Lorem ipsum</td><td>10</td><td>21</td><td>12</td><td>12</td></tr>
    <tr><td>Lorem ipsum</td><td>25</td><td>25</td><td>25</td><td>25</td></tr>
    <tr><td>Lorem ipsum</td><td>12</td><td>32</td><td>30</td><td>32</td></tr>
    <tr><td>Lorem ipsum</td><td>20</td><td>10</td><td>21</td><td>21</td></tr>
    <tr><td>Lorem ipsum</td><td>35</td><td>33</td><td>35</td><td>32</td></tr>
    <tr><td>Lorem ipsum</td><td>22</td><td>30</td><td>22</td><td>30</td></tr>
  </table>
  <footer class="foot"><span class="brand">STONECREST</span><span>© Copyright Stonecrest Properties</span><span class="mark"></span></footer>
</section>

<!-- 20 Our team four -->
<section class="slide num">
  <h2 class="title">Our Team</h2>
  <div class="person" style="left:16px;top:30px"><div class="face" style="width:26px;height:26px;flex:none" role="img" aria-label="Team member portrait"></div><div><h6>Michael Doe</h6><div class="role">CEO</div><p class="tiny">• Lorem ipsum dolor sit amet<br>• Sed do eiusmod tempor<br>• Ut enim ad minim</p></div></div>
  <div class="person" style="left:138px;top:30px"><div class="face" style="width:26px;height:26px;flex:none" role="img" aria-label="Team member portrait"></div><div><h6>James Doe</h6><div class="role">Manager</div><p class="tiny">• Lorem ipsum dolor sit amet<br>• Sed do eiusmod tempor<br>• Ut enim ad minim</p></div></div>
  <div class="person" style="left:16px;top:80px"><div class="face" style="width:26px;height:26px;flex:none" role="img" aria-label="Team member portrait"></div><div><h6>Jane Doe</h6><div class="role">Director</div><p class="tiny">• Lorem ipsum dolor sit amet<br>• Sed do eiusmod tempor<br>• Ut enim ad minim</p></div></div>
  <div class="person" style="left:138px;top:80px"><div class="face" style="width:26px;height:26px;flex:none" role="img" aria-label="Team member portrait"></div><div><h6>John Doe</h6><div class="role">Professor</div><p class="tiny">• Lorem ipsum dolor sit amet<br>• Sed do eiusmod tempor<br>• Ut enim ad minim</p></div></div>
  <footer class="foot"><span class="brand">STONECREST</span><span>© Copyright Stonecrest Properties</span><span class="mark"></span></footer>
</section>

<!-- 21 Testimonials -->
<section class="slide num">
  <h2 class="title">Customer Testimonials</h2>
  <div class="abs face" style="left:56px;top:26px;width:36px;height:36px" role="img" aria-label="Customer portrait"></div>
  <p class="tiny abs" style="left:110px;top:32px;width:136px">Adipiscing elit, sed diam nonummy nibh euismod tincidunt ut laoreet dolore magna aliquam erat volutpat. Ut wisi enim ad minim veniam.</p>
  <div class="abs" style="left:0;top:78px;width:260px;height:68px;background:var(--dark);display:grid;grid-template-columns:repeat(4,1fr);padding:8px 10px;text-align:center">
    <div><span class="ico" style="width:14px;height:14px;background:none;border:1px solid #fff"></span><p class="tiny w">Why does getting a loan have to be so hard?</p></div>
    <div><span class="ico" style="width:14px;height:14px;background:none;border:1px solid #fff"></span><p class="tiny w">Why do I have to go to a branch to get a quote?</p></div>
    <div><span class="ico" style="width:14px;height:14px;background:none;border:1px solid #fff"></span><p class="tiny w">Why do banks refuse to lend to me every month?</p></div>
    <div><span class="ico" style="width:14px;height:14px;background:none;border:1px solid #fff"></span><p class="tiny w">Why is there no lender that fits my needs?</p></div>
  </div>
</section>

<!-- 22 Two pictures -->
<section class="slide num">
  <h2 class="title">Two Pictures Slide</h2>
  <div class="abs ph warm" style="left:20px;top:28px;width:108px;height:98px;background:linear-gradient(160deg,#8e8a86,#3e3532 60%,#6f3a2c)" role="img" aria-label="Modern office interior with desks"></div>
  <div class="abs ph warm" style="left:134px;top:28px;width:108px;height:98px" role="img" aria-label="Reception area with red accents"></div>
  <footer class="foot"><span class="brand">STONECREST</span><span>© Copyright Stonecrest Properties</span><span class="mark"></span></footer>
</section>

<!-- 23 Title and image + text -->
<section class="slide num">
  <h2 class="title">Title and Image + Text</h2>
  <div class="abs ph warm" style="left:18px;top:26px;width:224px;height:52px;background:linear-gradient(180deg,#d9d3cc,#b67a5e 55%,#7c5a45)" role="img" aria-label="Row of residential townhouses"></div>
  <p class="abs" style="left:18px;top:86px;width:108px;font-size:4.2px;line-height:1.35;color:var(--red)">Lorem ipsum dolor sit amet, consectetur adipiscing elit, sed do eiusmod tempor incididunt ut labore et dolore magna aliqua. Ut enim ad minim veniam, quis nostrud.</p>
  <p class="tiny abs" style="left:134px;top:86px;width:108px">Lorem ipsum dolor sit amet, consectetur adipiscing elit, sed do eiusmod tempor incididunt ut labore et dolore magna aliqua. Duis aute irure dolor in reprehenderit in voluptate velit esse cillum dolore eu fugiat nulla pariatur.</p>
  <footer class="foot"><span class="brand">STONECREST</span><span>© Copyright Stonecrest Properties</span><span class="mark"></span></footer>
</section>

<!-- 24 Sales comparison -->
<section class="slide num">
  <h2 class="title">Sales Comparison</h2>
  <div class="abs" style="left:44px;top:38px;font-size:3.5px;color:#333">2018 Sales</div>
  <svg class="abs" style="left:16px;top:44px" width="80" height="46" viewBox="0 0 80 46">
    <g fill="var(--red)"><rect x="4" y="10" width="5" height="32"/><rect x="24" y="24" width="5" height="18"/><rect x="44" y="22" width="5" height="20"/><rect x="64" y="8" width="5" height="34"/></g>
    <line x1="0" y1="42" x2="80" y2="42" stroke="#ccc" stroke-width=".5"/>
  </svg>
  <div class="abs" style="left:20px;top:96px;font-size:10px;color:var(--red);font-weight:300">45%</div>
  <p class="tiny abs" style="left:48px;top:97px;width:50px"><span style="color:var(--red)">Lorem ipsum dolor</span><br>Sit amet consectetur.</p>
  <div class="abs" style="left:128px;top:30px;height:90px;border-left:1px dashed #ccc"></div>
  <div class="abs" style="left:120px;top:70px;width:17px;height:17px;border-radius:50%;background:#111;color:#fff;font-size:4.5px;display:flex;align-items:center;justify-content:center">VS</div>
  <div class="abs" style="left:192px;top:38px;font-size:3.5px;color:#333">2019 Sales</div>
  <svg class="abs" style="left:166px;top:44px" width="80" height="46" viewBox="0 0 80 46">
    <g fill="var(--dark)"><rect x="4" y="10" width="5" height="32"/><rect x="24" y="22" width="5" height="20"/><rect x="44" y="16" width="5" height="26"/><rect x="64" y="8" width="5" height="34"/></g>
    <line x1="0" y1="42" x2="80" y2="42" stroke="#ccc" stroke-width=".5"/>
  </svg>
  <div class="abs" style="left:168px;top:96px;font-size:10px;color:var(--dark);font-weight:300">68%</div>
  <p class="tiny abs" style="left:196px;top:97px;width:50px"><span style="color:var(--dark)">Lorem ipsum dolor</span><br>Sit amet consectetur.</p>
  <footer class="foot"><span class="brand">STONECREST</span><span>© Copyright Stonecrest Properties</span><span class="mark"></span></footer>
</section>

</main>
</body>
</html>
```